Automotive parts Package (box) design

We are developing a new packaging concept for our automotive service and suspension parts line. I will share 2–3 sample designs—some from other brands and some AI‑generated—and we need a designer to create a unified, original design direction based on these references.

We already have an established brand name, KEM, along with a logo. The logo may be updated or redesigned, but the brand name KEM must remain.

- The project includes creating the full packaging design for our product boxes, developing or refining the logo if needed.

-Then, after choosing the design, we will apply the same design to 8 boxes with small customisation for each box to match the product.

- The box die-lines will be provided by us.

Attached are a few sample designs. We need you to develop three or more new designs in a similar style. If you have additional creative concepts beyond these references, you are welcome to include them. The only fixed requirement is that the brand name KEM must remain unchanged in all proposed designs.

Box files such as PNG, PDF (ready-to-print file) and Ai (Editable/ Source file) and fonts with 3D mockup images at the end of the project must be given to us.

Target Market(s)

Car spare parts shops

Industry/Entity Type

Auto Parts

Requirements
Must have
• Our brand name KEM
Nice to have
• Package similar to big auto parts suppliers such as PLW, VARNE

```html
<!DOCTYPE html>
<html lang="en">
<head>
<meta charset="utf-8">
<title>KEM Ball Joint – Box Panels</title>
<link rel="stylesheet" href="https://fonts.googleapis.com/css2?family=Archivo+Black&family=Montserrat:wght@500;600;700&display=swap">
<style>
  :root{
    --red:#c8202a;
    --red-dark:#9e1820;
    --ink:#2b2b2b;
    --black:#141414;
    --white:#ffffff;
    --bg:#e9e9ea;
    --gold:#d9a935;
  }
  *{margin:0;padding:0;box-sizing:border-box}
  html,body{width:1200px;height:417px;overflow:hidden;background:var(--bg)}
  body{font-family:"Montserrat",sans-serif;position:relative}
  .panel{position:absolute;overflow:hidden}
  .top{left:15px;top:15px;width:725px;height:70px;background:var(--red);color:var(--white);text-align:center}
  .front{left:15px;top:95px;width:540px;height:307px;background:var(--white)}
  .side{left:570px;top:95px;width:170px;height:307px;background:var(--black);color:var(--white)}
  .base{left:755px;top:15px;width:430px;height:387px;background:var(--red);color:var(--white)}
  .front-art{position:absolute;inset:0;width:100%;height:100%}
  .brand{font-family:"Archivo Black",sans-serif;line-height:1}
  .tagline{font-size:7px;font-weight:700;letter-spacing:2.4px}
  .top .brand{margin-top:10px;font-size:36px;color:var(--white);letter-spacing:2px}
  .top .tagline{margin-top:5px;color:var(--white)}
  .front .brand{position:absolute;left:22px;top:22px;font-size:52px;color:var(--red);letter-spacing:1px}
  .front .tagline{position:absolute;left:24px;top:78px;color:var(--ink)}
  .title{position:absolute;left:22px;top:100px;font-family:"Archivo Black",sans-serif;font-size:36px;line-height:.95;color:var(--ink)}
  .title span{display:block;color:var(--red)}
  .category{position:absolute;left:22px;top:176px;width:230px;height:22px;background:var(--red);color:var(--white);font-size:7px;font-weight:600;letter-spacing:1.6px;padding:7px 0 0 14px}
  .features{position:absolute;left:22px;top:208px;display:flex}
  .feature{width:76px;text-align:center;font-size:6.5px;font-weight:600;letter-spacing:1.4px;color:var(--ink);border-right:1px solid #bbb;padding:0 6px}
  .feature:last-child{border-right:0}
  .feature svg{display:block;margin:0 auto 5px;width:30px;height:30px}
  .front-band{position:absolute;left:0;bottom:12px;width:100%;height:28px;background:var(--red);color:var(--white);font-size:7px;font-weight:600;letter-spacing:1.8px;padding:10px 0 0 22px}
  .seal{position:absolute;left:200px;top:40px;width:76px;height:76px;border-radius:50%;background:radial-gradient(circle,#f4d47a,var(--gold) 70%,#a97a1c)}
  .product{position:absolute;left:330px;top:24px;width:110px;height:222px;border-radius:28px;background:linear-gradient(90deg,#6f7377,#e6e8ea 45%,#8a8e92)}
  .side .brand{position:absolute;left:0;right:0;top:20px;text-align:center;font-size:30px;color:var(--white)}
  .side .tagline{position:absolute;top:55px;width:100%;text-align:center;color:var(--white);font-size:5px;letter-spacing:1.4px}
  .side-title{position:absolute;top:72px;width:100%;text-align:center;font-family:"Archivo Black",sans-serif;font-size:15px;color:var(--red)}
  .side-sub{position:absolute;top:94px;width:100%;text-align:center;font-size:6px;font-weight:600;letter-spacing:1px;line-height:1.5}
  .side-list{position:absolute;top:124px;left:0;width:100%;list-style:none;text-align:center}
  .side-list li{margin-bottom:9px;font-size:5.5px;font-weight:700;letter-spacing:1px}
  .side-list svg{display:block;margin:0 auto 4px;width:16px;height:16px}
  .side-list small{display:block;color:var(--red);font-size:5px;font-weight:500;margin-top:2px;letter-spacing:.4px}
  .side-band{position:absolute;bottom:12px;left:0;width:100%;height:28px;background:var(--red)}
  .notice{position:absolute;top:70px;width:100%;text-align:center}
  .notice h2{font-weight:700;font-size:17px;letter-spacing:4px;margin-bottom:10px}
  .notice h3{font-size:8px;font-weight:700;letter-spacing:2px;margin-bottom:8px}
  .notice p{font-size:8px;font-weight:500;letter-spacing:1.6px;line-height:1.55;width:360px;margin:0 auto}
  .base-icons{position:absolute;top:260px;width:100%;display:flex;justify-content:center;gap:46px}
  .base-icons svg{width:46px;height:46px}
</style>
</head>
<body>
<section class="panel top">
  <div class="brand">KEM</div>
  <div class="tagline">AUTOMOTIVE COMPONENTS</div>
</section>

<section class="panel front">
  <svg class="front-art" viewBox="0 0 540 307" preserveAspectRatio="none">
    <defs><linearGradient id="darkfade" x1="0" y1="0" x2="1" y2="1"><stop offset="0" stop-color="#2a2a2a"/><stop offset="1" stop-color="#0c0c0c"/></linearGradient></defs>
    <path d="M190 0H540V307H285L262 260C275 220 240 120 190 0Z" fill="url(#darkfade)"/>
    <path d="M0 0H540V8H0Z" fill="var(--red)"/>
  </svg>
  <div class="brand">KEM</div>
  <div class="tagline">AUTOMOTIVE COMPONENTS</div>
  <h1 class="title">BALL<span>JOINT</span></h1>
  <div class="category">STEERING &amp; SUSPENSION PARTS</div>
  <div class="features">
    <div class="feature"><svg viewBox="0 0 36 36"><circle cx="18" cy="18" r="16" fill="none" stroke="var(--red-dark)" stroke-width="2"/><path d="M10 15L14 10H22L26 15L18 26Z" fill="var(--red-dark)"/></svg>PREMIUM QUALITY</div>
    <div class="feature"><svg viewBox="0 0 36 36"><circle cx="18" cy="18" r="15" fill="none" stroke="var(--red-dark)" stroke-width="4" stroke-dasharray="4 3"/><path d="M18 9L25 12V18C25 23 18 27 18 27C18 27 11 23 11 18V12Z" fill="var(--red-dark)"/><path d="M14.5 18L17 20.5L22 15" stroke="#fff" stroke-width="2" fill="none"/></svg>HIGH DURABILITY</div>
    <div class="feature"><svg viewBox="0 0 36 36"><path d="M8 26A12 12 0 1 1 28 26" fill="none" stroke="var(--red-dark)" stroke-width="2.5"/><path d="M18 22L24 13" stroke="var(--red-dark)" stroke-width="2.5"/><circle cx="18" cy="22" r="2.5" fill="var(--red-dark)"/></svg>SMOOTH PERFORMANCE</div>
  </div>
  <div class="seal" role="img" aria-label="Quality guarantee seal"></div>
  <div class="product" role="img" aria-label="Chrome ball joint product render"></div>
  <div class="front-band">PRECISION ENGINEERED &#8226; BUILT FOR SAFETY &#8226; DESIGNED FOR PERFORMANCE</div>
</section>

<section class="panel side">
  <div class="brand">KEM</div>
  <div class="tagline">AUTOMOTIVE COMPONENTS</div>
  <div class="side-title">BALL JOINT</div>
  <div class="side-sub">ENGINEERED FOR<br>CONFIDENT CONTROL</div>
  <ul class="side-list">
    <li><svg viewBox="0 0 18 18"><path d="M9 1L16 4V9C16 13 9 17 9 17C9 17 2 13 2 9V4Z" fill="none" stroke="#fff" stroke-width="1.5"/></svg>RELIABLE SAFETY<small>Tested for lasting road grip</small></li>
    <li><svg viewBox="0 0 18 18"><circle cx="9" cy="9" r="7" fill="none" stroke="#fff" stroke-width="2.5" stroke-dasharray="3 2"/></svg>DURABLE CONSTRUCTION<small>Built to resist wear daily</small></li>
    <li><svg viewBox="0 0 18 18"><path d="M3 14A7 7 0 1 1 15 14" fill="none" stroke="#fff" stroke-width="1.5"/><path d="M9 11L12 6" stroke="#fff" stroke-width="1.5"/></svg>PRECISE PERFORMANCE<small>Exact fit for smooth steering</small></li>
  </ul>
  <div class="side-band"></div>
</section>

<section class="panel base">
  <div class="notice">
    <h2>INSTALLATION NOTICE</h2>
    <h3>PROFESSIONAL INSTALLATION IS RECOMMENDED.</h3>
    <p>ALWAYS VERIFY VEHICLE COMPATIBILITY AND PART NUMBER BEFORE INSTALLATION. INSTALLATION SHOULD BE PERFORMED ACCORDING TO THE VEHICLE MANUFACTURER'S RECOMMENDED PROCEDURES.</p>
  </div>
  <div class="base-icons">
    <svg viewBox="0 0 46 46" aria-label="Recyclable"><g fill="none" stroke="#fff" stroke-width="4"><path d="M17 10L23 4L29 14"/><path d="M38 24L41 33H29"/><path d="M16 39H7L12 28"/></g><path d="M26 10L33 12L31 19Z M25 33L30 38V28Z M13 22L8 17L17 19Z" fill="#fff"/></svg>
    <svg viewBox="0 0 46 46" aria-label="Dispose responsibly"><g fill="none" stroke="#fff" stroke-width="3"><path d="M8 12H38M18 12V7H28V12M11 12L14 40H32L35 12M19 19V33M23 19V33M27 19V33"/></g></svg>
    <svg viewBox="0 0 46 46" aria-label="Quality approved"><circle cx="23" cy="23" r="19" fill="none" stroke="#fff" stroke-width="3"/><circle cx="23" cy="23" r="13" fill="#fff"/><path d="M17 23L21 27L29 18" stroke="var(--red)" stroke-width="3" fill="none"/></svg>
  </div>
</section>
</body>
</html>
```